Urgent - brand new business card for a startup technical advisory and incubation business in Sydney

We need a brand new business card design for BrightForge. We are a startup technical advisory and incubation business based in Sydney Australia. We work with entrepreneurs and innovators to help rapidly and efficiently turn their ideas into reality and to ensure they have the technical platform required for growth.

Our name is partly inspired by our love of lean product development methods and the lean startup movement.

We would like clean, uncluttered designs that feature our two logo colours and communicate a professional but creative, in-touch and entrepreneurial business.

PLEASE SEE MUST HAVE PRIORITIES FOR DRAFT CONTACT INFORMATION AND OTHER DESIRED TEXT ON CARD.
Updates

We have now updated the brief to include draft business card contact information and also some additional desired text to feature on the card design.    Please review the Must Have priorities.

Also final updated source files for the horizontal and vertical versions have now been uploaded and should be used for any designs.

Thanks!

Target Market(s)

Entrepeneurs, innovators, startup investors looking for a strong product development partner

Industry/Entity Type

Business

Requirements
Must have
• Feature our two logo colours
Be a relatively clean, pared back overall design - quite minimalist

Updated source files (AI) for vertical and horizontal layouts attached.

Draft contact information for business card:
Tom Harcourt
Founder & CTO
Phone: +61 427 555123
Email: xxxx@brightforge.example
Skype: xxxxxharcourt
Twitter: tharcourt

www.brightforge.example

We would also like the overall design to include the phrase "You have great ideas. Let us make them happen." (probably in a reasonably subtle way)

Nice to have
• Inspire me! Double-sided designs are fine with logo, phrase, (URL?) on one side and contact details on other (+ any other design elements)

Logo on business card can be either with lightbulb above the wording as per example here or to the left of the BrightForge wording - both layouts in files provided.
Should not have
• Shouldn't look like a Pendrel Suite business card template :-)

```html
<!DOCTYPE html>
<html lang="en">
<head>
<meta charset="utf-8">
<title>BrightForge Business Card</title>
<link rel="stylesheet" href="https://fonts.googleapis.com/css2?family=Advent+Pro:wght@300;400;600&display=swap">
<style>
  :root {
    --backdrop: #ececec;
    --card-white: #ffffff;
    --card-navy: #13232f;
    --brand-cyan: #17a8e0;
    --text-white: #f2f5f7;
    --watermark: rgba(255, 255, 255, 0.10);
    --icon-tile: #d9eef8;
    --note-blue: #2ba3da;
  }
  * { margin: 0; padding: 0; box-sizing: border-box; }
  html, body {
    width: 1200px; height: 1000px; overflow: hidden;
    background: var(--backdrop);
    font-family: "Advent Pro", "Arial Narrow", sans-serif;
  }
  .sheet { position: relative; width: 1200px; height: 1000px; }

  .card {
    position: absolute;
    border-radius: 34px;
  }
  .card-front {
    left: 50px; top: 90px; width: 780px; height: 390px;
    background: var(--card-white);
    z-index: 2;
    display: flex; flex-direction: column; align-items: center; justify-content: center;
  }
  .brand-dot {
    width: 118px; height: 118px; border-radius: 50%;
    background: var(--brand-cyan);
    margin-bottom: 26px;
  }
  .brand-name {
    font-weight: 600;
    font-size: 78px;
    line-height: 1;
    color: var(--brand-cyan);
    letter-spacing: -1px;
  }

  .card-back {
    left: 350px; top: 470px; width: 780px; height: 360px;
    background: var(--card-navy);
    z-index: 1;
  }
  .watermark {
    position: absolute; left: 70px; top: 50px; width: 220px;
    display: flex; flex-direction: column; align-items: center;
  }
  .watermark-dot {
    width: 92px; height: 92px; border-radius: 50%;
    background: var(--watermark);
    margin-bottom: 22px;
  }
  .watermark-name {
    font-weight: 600; font-size: 54px; line-height: 1;
    color: var(--watermark); letter-spacing: -1px;
  }
  .identity {
    position: absolute; left: 330px; top: 100px;
    display: flex; align-items: baseline; gap: 22px;
  }
  .person-name { font-weight: 400; font-size: 40px; color: var(--brand-cyan); }
  .person-title { font-weight: 400; font-size: 25px; color: var(--text-white); letter-spacing: 1px; }
  .contacts {
    position: absolute; left: 326px; top: 178px;
    list-style: none;
  }
  .contacts li {
    display: flex; align-items: center; gap: 10px;
    height: 29px;
    font-size: 25px; font-weight: 300; color: var(--brand-cyan);
  }
  .icon {
    width: 20px; height: 20px; border-radius: 3px;
    background: var(--icon-tile);
    flex: none; display: block;
  }

  .print-notes {
    position: absolute; left: 44px; top: 842px;
    font-size: 23px; font-weight: 300; line-height: 31px;
    color: var(--note-blue);
  }
</style>
</head>
<body>
<main class="sheet">
  <section class="card card-back" aria-label="Card back, contact side">
    <div class="watermark" aria-hidden="true">
      <div class="watermark-dot"></div>
      <div class="watermark-name">BrightForge</div>
    </div>
    <div class="identity">
      <h1 class="person-name">Tom Harcourt</h1>
      <p class="person-title">Founder &amp; CTO</p>
    </div>
    <ul class="contacts">
      <li>
        <svg class="icon" viewBox="0 0 20 20" aria-label="Phone"><rect width="20" height="20" rx="3" fill="#d9eef8"/><rect x="6" y="3" width="8" height="14" rx="1.5" fill="#1b8fc4"/><rect x="7.3" y="5" width="5.4" height="8" fill="#d9eef8"/></svg>
        +61 427 555123
      </li>
      <li>
        <svg class="icon" viewBox="0 0 20 20" aria-label="Email"><rect width="20" height="20" rx="3" fill="#d9eef8"/><rect x="3" y="5" width="14" height="10" fill="#ffffff" stroke="#7fa9bd"/><path d="M3 5 L10 11 L17 5" fill="none" stroke="#7fa9bd"/></svg>
        xxxx@brightforge.example
      </li>
      <li><span class="icon" aria-label="Chat handle"></span>xxxxxharcourt</li>
      <li><span class="icon" aria-label="Social handle"></span>tharcourt</li>
    </ul>
  </section>

  <section class="card card-front" aria-label="Card front, brand side">
    <div class="brand-dot" aria-hidden="true"></div>
    <div class="brand-name">BrightForge</div>
  </section>

  <div class="print-notes">
    <p>Namecard Round Corner Cut</p>
    <p>Size: 9cm(h)x4.5cm(w)</p>
    <p>Front Cover &nbsp;: 1 Tonematch7547 + C85</p>
    <p>Back Cover &nbsp;: 1 Tonematch7547 + C85 (logo- white 10% light watermark effect)</p>
  </div>
</main>
</body>
</html>
```